A Writer With A Website (Writes action/mysteries with a touch of romance thrown in)

I need a website. I am an unpublished writer. I own a domain and tried a bit to design one in Wordpress. I would like to be able to change out pictures, blog, and receive email. My fav color is orange (but not necessary in website) I like the font "Hello Stockholm" Probably 4 or five different pages. Attached is a poor scan of a business card.
Updates

Had a recent death in the family, my inspiration to get the site designed and also the reason I may need a few days.

I write books action mysteries. So far all take place in Wyoming. I realize there was not much info given. Pages: Home, Looking for representation, recommended reading and other things I like, Mirabel (a page dedicated to my daughter who just passed away), and other useful links. Probably shorter ways to say those, but you get the idea.

Thanks for the designs submitted. I know I gave very little direction. There are a few authors who write in Wyoming who are popular, RT Haskell, Dwight Fenner (Ashcroft Saga) I would argue that the main character in any of their books is Wyoming, or the West. No cliches. Cowboy hats, horses, not so good. For those outside the US, maybe do a serch on Wyoming and look at the pictures. I have photo's for possible use in my design, will post them tonight. Thanks all. -k-

I am not sure how much info gets added, how much the designer does and how I fill in the "blanks". Here is partial text for the "Mirabel" page: Over the years, our daughters’ friends overlapped one another and two or three became like daughters to Loreen and me. Some even became our friends as they grew into adulthood. One had a father who tried to committed suicide multiple times. After one attempt she asked him, “why?” He said, “I am glad you can’t understand why, only someone who can travel to that dark a place can understand why”. He was eventually successful. She shared that story with us on August 14th when our daughter Mirabel found that dark place in herself and took her life. We found a suicide note, then her body, then everything went into a fog. An hour or so later, my wife and I stood on the front lawn after the police interviews and watched as the corner slide a covered corpse into the white SUV with darkened windows. We stood there as the rain began to fall, and the sky sobbed with us. As they closed the back of the coroner’s Suburban, the rain fell harder and harder and a fireman guided us back into the house that will never be the same for us.

Target Market(s)

Currently trying to get an agent, this is to look like I have followers.

Number of Pages Required

5+ page

Font styles to use
Serif

Colors
f68e4e

Requirements
Nice to have
• I like orange (more of a burnt orange color) I am a big fan of Matthias Dorrel. A "feel" like that might be nice. I am from Wyoming, That rugged western culture shows up in all my writing.
Should not have
• Western Cliche,

```html
<!DOCTYPE html>
<html lang="en">
<head>
<meta charset="utf-8">
<title>Wade K Marlow — Author</title>
<link href="https://fonts.googleapis.com/css2?family=Herr+Von+Muellerhoff&family=Josefin+Sans:wght@400;600&family=EB+Garamond:wght@400;700&display=swap" rel="stylesheet">
<style>
:root{
  --white:#ffffff;
  --ink:#2b2118;
  --body:#5a4a3a;
  --cream:#f2dca0;
  --mint:#e9ebbe;
  --tan:#eab57c;
  --band:#d9b24a;
  --footer:#80614a;
  --footer-text:#f4ead8;
  --script:"Herr Von Muellerhoff", cursive;
  --caps:"Josefin Sans", sans-serif;
  --serif:"EB Garamond", serif;
}
*{margin:0;padding:0;box-sizing:border-box}
html,body{width:1200px;height:3789px;overflow:hidden}
body{position:relative;font-family:var(--serif);color:var(--body);background:var(--white)}
section,header,footer{position:absolute;left:0;width:1200px}
.abs{position:absolute}
.script{font-family:var(--script);font-weight:400;color:var(--ink);line-height:1.1;white-space:nowrap}
.caps{font-family:var(--caps);text-transform:uppercase;letter-spacing:1.5px}
p.copy{font-size:17px;line-height:28px}
.more{font-family:var(--caps);font-size:14px;font-weight:600;letter-spacing:1px;color:var(--ink);text-transform:uppercase}

/* hero */
.hero{top:0;height:707px;background:linear-gradient(180deg,#3d3f86 0%,#7c4c8a 18%,#c9364a 36%,#f06a3a 48%,#b0567c 58%,#5a5a9a 66%,#3f5a3a 76%,#6f8b3a 88%,#8a9a48 100%)}
.logo{left:50px;top:48px;font-family:var(--script);font-size:86px;line-height:1.1;color:var(--white);white-space:nowrap}
.nav{right:74px;top:92px;display:flex;gap:30px;font-family:var(--caps);font-size:24px;color:var(--white);letter-spacing:1.5px;text-transform:uppercase}
.hero-title{left:115px;top:360px;font-family:var(--script);font-weight:400;font-size:140px;line-height:110px;color:var(--white);white-space:nowrap}
.hero-title span{display:block;padding-left:190px}

/* about */
.about{top:707px;height:638px;background:linear-gradient(180deg,#e2cc5c,#cdb452 60%,#d6c49a)}
.about-side{left:0;top:0;width:417px;height:638px;background:linear-gradient(180deg,rgba(150,120,60,.35),rgba(180,150,90,.25))}
.about h2{left:88px;top:92px;font-size:100px}
.photo{background:linear-gradient(135deg,#6b5a44,#3b342e 60%,#a08a6c)}
.about .p1{left:93px;top:208px;width:278px;height:368px}
.about .col-title{left:450px;top:68px;font-size:72px;border-bottom:2px solid var(--ink);padding-right:4px}
.about .sub{left:480px;top:184px;font-size:20px;color:var(--ink)}
.about .col-copy{left:480px;top:240px;width:340px}
.about .p2{left:462px;top:346px;width:371px;height:255px;background:linear-gradient(135deg,#e6e4e0,#9a9894 45%,#5a3f2a 60%,#3a2a20)}
.about .list{left:879px;top:86px;width:300px}
.about .list h3{font-family:var(--caps);text-transform:uppercase;font-weight:400;font-size:20px;letter-spacing:1.5px;color:var(--ink);margin-top:14px}
.about .list h3:first-child{margin-top:0}
.about .list p{font-size:17px;line-height:28px;margin-top:10px}

/* welcome */
.welcome{top:1345px;height:378px;background:var(--cream);text-align:center}
.welcome h2{position:absolute;left:0;width:100%;top:48px;font-size:104px;line-height:1}
.welcome .copy{position:absolute;left:96px;width:1010px;top:168px;font-size:15px;line-height:21px;color:var(--ink)}
.welcome .more{position:absolute;left:0;width:100%;top:302px}

/* mixed */
.mixed{top:1723px;height:576px;background:var(--mint)}
.mixed h2{font-size:62px;top:50px}
.mixed .quote{left:88px;top:268px;font-size:24px;line-height:46px;color:var(--ink)}
.mixed .sub{left:644px;top:218px;font-size:17px;color:var(--ink)}
.mixed .tea{left:644px;top:267px;width:526px;height:246px;background:linear-gradient(135deg,#6e6c68,#d8d4cc 40%,#8a8680 70%,#e8e6e2)}

/* dark */
.dark{top:2299px;height:543px;background:linear-gradient(135deg,#2a2622,#3a352e 50%,#161412)}
.dark .p3{left:38px;top:101px;width:530px;height:348px;background:linear-gradient(180deg,#c26a38 0%,#e09a4a 30%,#4d6a2a 60%,#8a6a3a 80%,#6d7a3a 100%)}
.dark .item{left:647px;width:520px}
.dark h3{font-family:var(--caps);text-transform:uppercase;font-weight:400;font-size:22px;letter-spacing:1.5px;color:var(--white)}
.dark p{font-size:17px;line-height:28px;color:#cfc6b8;margin-top:12px}

/* tan */
.tan{top:2842px;height:606px;background:var(--tan)}
.tan h2{font-size:66px}
.tan .p4{left:677px;top:55px;width:498px;height:192px;background:linear-gradient(135deg,#8a7a6a,#d8d2cc 45%,#eae6e2 70%,#7a5a4a)}

.band{top:3448px;height:25px;background:var(--band)}

/* footer */
.footer{top:3473px;height:316px;background:var(--footer);color:var(--footer-text)}
.footer .logo{left:50px;top:22px;font-size:92px}
.footer .addr{left:101px;top:152px;font-size:15px;line-height:30px;font-weight:700}
.footer .maps{left:101px;top:240px;font-size:12px;font-weight:700;letter-spacing:.5px}
.footer h4{font-size:16px;font-weight:700;margin-bottom:20px}
.footer ul{list-style:none;font-size:14px;font-weight:700;line-height:20px;letter-spacing:.5px}
.footer .about-text{font-size:14px;font-weight:700;line-height:22px}
.footer .read{font-size:12px;font-weight:700;margin-top:24px}
</style>
</head>
<body>

<header class="hero" role="img" aria-label="Sunset over Wyoming mountain range and valley">
  <div class="abs logo">Wade K Marlow</div>
  <nav class="abs nav"><span>Literature</span><span>Writing</span><span>About me</span><span>Contact</span></nav>
  <h1 class="abs hero-title">Can you guess<span>the mystery?</span></h1>
</header>

<section class="about">
  <div class="abs about-side"></div>
  <h2 class="abs script">About me</h2>
  <div class="abs photo p1" role="img" aria-label="Ink pot, glasses and open notebook on a wooden desk"></div>
  <div class="abs script col-title">Per existent est quod</div>
  <div class="abs caps sub">Et ipsum quodque</div>
  <p class="abs copy col-copy">Sed in dui in augue consectetur lobortis. Pellentesque orci tellus, imperdiet interdum nibh a, varius gravida augue.</p>
  <div class="abs p2" role="img" aria-label="Open notebook and pen on dark wood"></div>
  <div class="abs list">
    <h3>Nunnus et quod</h3>
    <p>Lorem ipsum dolor sit amet, consectetur adipiscing elit. Praesent</p>
    <h3>Quoque serat</h3>
    <p>Lorem ipsum dolor sit amet, consectetur adipiscing elit. Praesent hendrerit quis enim se vehicula. Sed in</p>
    <h3>Adisperi et forma</h3>
    <p>Lorem ipsum dolor sit amet, consectetur adipiscing elit. Praesent</p>
    <h3>Quod expergit</h3>
    <p>Lorem ipsum dolor sit amet, consectetur adipiscing elit. Praesent</p>
  </div>
</section>

<section class="welcome">
  <h2 class="script">Welcome to my site</h2>
  <p class="copy">Pellentesque habitant morbi tristique senectus et netus et malesuada fames ac turpis egestas. Curabitur est erat, eleifend ut dignissim a, imperdiet ac leo. Morbi tincidunt nulla ut massa vehicula, eu porta dolor feugiat. Lorem ipsum dolor sit amet, consectetur adipiscing elit. Donec gravida gravida leo, convallis consectetur libero pulvinar sit amet. Interdum et malesuada fames ac ante ipsum primis in faucibus. Donec quis vulputate mi.</p>
  <div class="more">Know more</div>
</section>

<section class="mixed">
  <h2 class="abs script" style="left:88px">Vulpus Elit</h2>
  <p class="abs copy" style="left:88px;top:126px;width:518px">Quisque tincidunt quam a porta sagittis. Etiam at urna dolor. Curabitur semper, arcu ut consequat sagittis, arcu purus venenatis est, et tristique nibh nibh porttitor odio. Nunc blandit ac ante in</p>
  <p class="abs quote">“eternatitem magistima chose<br>perception randa quod vivendum<br>et se quanda scit…”</p>
  <h2 class="abs script" style="left:644px">Perpit Perptlena</h2>
  <p class="abs copy" style="left:644px;top:126px;width:530px">Quisque tincidunt quam a porta sagittis. Etiam at urna dolor. Curabitur semper, arcu ut consequat sagittis, arcu purus venenatis est, et tristique nibh nibh porttitor odio. Nunc blandit ac ante in</p>
  <div class="abs caps sub">Eternitatem magistima chose</div>
  <div class="abs tea" role="img" aria-label="Cup of tea, daisies and open book on a grey table"></div>
</section>

<section class="dark" role="img" aria-label="Dim background of an open book">
  <div class="abs p3" role="img" aria-label="Wyoming pond and pine trees at sunset"></div>
  <div class="abs item" style="top:48px"><h3>Tincidunt quam sert</h3><p>Quisque tincidunt quam a porta sagittis. Etiam at urna dolor. Curabitur semper, arcu ut consequat sagittis, arcu purus venenatis est, et tristique nibh nibh porttitor odio. Nunc blandit ac ante in</p></div>
  <div class="abs item" style="top:202px"><h3>Et quique potest</h3><p>Quisque tincidunt quam a porta sagittis. Etiam at urna dolor. Curabitur semper, arcu ut consequat sagittis, arcu purus venenatis est, et tristique nibh nibh porttitor odio. Nunc blandit ac ante in</p></div>
  <div class="abs item" style="top:354px"><h3>Perpendiculae vitae</h3><p>Quisque tincidunt quam a porta sagittis. Etiam at urna dolor. Curabitur semper, arcu ut consequat sagittis, arcu purus venenatis est, et tristique nibh nibh porttitor odio. Nunc blandit ac ante in</p></div>
</section>

<section class="tan">
  <h2 class="abs script" style="left:96px;top:62px">Per sciend scit</h2>
  <p class="abs copy" style="left:96px;top:142px;width:460px">Sed in dui in augue consectetur lobortis. Pellentesque orci tellus, imperdiet interdum nibh a, varius gravida augue. Curabitur faucibus, lectus vitae maximus scelerisque, nunc arcu molestie erat, congue efficitur</p>
  <h2 class="abs script" style="left:96px;top:300px">Quod melius</h2>
  <p class="abs copy" style="left:96px;top:382px;width:460px">Sed in dui in augue consectetur lobortis. Pellentesque orci tellus, imperdiet interdum nibh a, varius gravida augue. Curabitur faucibus, lectus vitae maximus scelerisque, nunc arcu molestie erat, congue efficitur ut enim eget mi. Phasellus id felis</p>
  <div class="abs p4" role="img" aria-label="Coffee cup beside a stack of books by a window"></div>
  <h2 class="abs script" style="left:677px;top:276px">Magis nihil verindum</h2>
  <p class="abs copy" style="left:677px;top:356px;width:500px">Quisque tincidunt quam a porta sagittis. Etiam at urna dolor. Curabitur semper, arcu ut consequat sagittis, arcu purus venenatis est, et tristique nibh nibh porttitor odio. Nunc blandit ac ante in accumsan. Vestibulum ac tincidunt eros. Suspendisse elementum</p>
  <div class="abs more" style="left:677px;top:494px">Know more</div>
</section>

<div class="abs band" style="left:0;width:1200px"></div>

<footer class="footer">
  <div class="abs logo">Wade K Marlow</div>
  <p class="abs addr">Lipsum quoque 10, et per<br>23, perque, Et sit</p>
  <div class="abs maps">SEE ON MAPS</div>
  <div class="abs" style="left:472px;top:90px">
    <h4>Links</h4>
    <ul><li>HOME</li><li>PORTFOLIO</li><li>SERVICES</li><li>ABOUT</li><li>CONTACT</li></ul>
  </div>
  <div class="abs" style="left:657px;top:90px;width:240px">
    <h4>About us</h4>
    <p class="about-text">Suspendisse aliquet purus et lectus consequat, vel auctor ante auctor. Nam et sapien</p>
    <p class="read">READ MORE</p>
  </div>
  <div class="abs" style="left:1023px;top:90px">
    <h4>More</h4>
    <ul><li>PHARETRA</li><li>ECIT</li><li>PERQUE</li><li>ED SAE</li><li>QUOQUE</li></ul>
  </div>
</footer>

</body>
</html>
```